Flyer-Design für ein Ingenieur- und Planungsbüro
Ein toller Entwurf und freundliche Kommunikation inkl. immer schneller Reaktionszeit, auch wenn es bei mir manchmal mit der Zuarbeit der passenden Bilder gedauert hat. Perfektes Ergebnis!!
Zielgruppe
Ingenieur- und Planungsbüro (Dienstleister) aus Leipzig, welches seit 22 Jahren auf die Optimierung und Neuerrichtung
medizinischer Einrichtungen (Arzt- und Zahnarztpraxen) spezialisiert ist.
Zur Zielgruppe zählen daher Mediziner und Zahnmedizinen zwischen 30 - 55 Jahren, welche bereits eine Praxis führen oder gerade neu gründen möchten. Die Schnittmenge liegt im Praxisstandort = Praxisräume, welche niedergelassene Mediziner zur Ausübung ihrer Tätigkeiten inkl. Personal, Medizintechnik und sonstige Ausstattung benötigen. Der Verkauf von Produkten und Einrichtungen ist nicht meine Aufgabe.
Meine Tätigkeiten liegen in der Beratung, Unterstützung der Medizinerinnen über das gesamte Projekt, von der ersten Idee, über die Umsetzung bis zur Praxiseröffnung. Ich bin daher Lotse, Koordinator aller Projektschnittstellen sowie Planer zur Umsetzung der jeweiligen Kundenanforderungen. Die Leistungsdetails und Stichpunkte sind den Unterlagen zu entnehmen oder weiter zu erfragen.
Aufgabenstellung
Der Flyer soll nach einem telefonischen Erstkontakt oder nach einem persönlichen Treffen meinen potenziellen Kunden einen Überblick zu den Umfangreichen Leistungsportfolio geben. Der Flyer soll professionell und seriös wirken und meine langjährige Expertise und Knowhow vermitteln.
Weiterhin soll der Flyer meinen Netzwerkpartner dienen, welche ebenfalls mit der Zielgruppe der Heilberufe im geschäftlichen Kontakt sind und mich über den Flyer im Gespräch weiterempfehlen und zu einem Neukontakt zwischen dem potenziellen Kunden/ Kundin führen soll.
Der in den Daten zur Verfügung gestellt Entwurf des Flyers braucht nicht 1:1 nachgebaut werden. Er bietet vielmehr eine Orientierung wie ich mir einen Flyer vorstellen kann. Auch die zur Verfügung gestellten Bilden dienen zur Orientierung, ggf. werden diese nach Feststellung des Siegers/ Siegerin im Detail nochmals angepasst.
Farben:
Blau: 041-171-226 / #29abe2
Grün: 140-198-063 / #8cc63f

```html
<!DOCTYPE html>
<html lang="de">
<head>
<meta charset="utf-8">
<title>Praxisbau Lotse UG – Flyer</title>
<link href="https://fonts.googleapis.com/css2?family=Catamaran:wght@300;400&family=Open+Sans:wght@400&display=swap" rel="stylesheet">
<style>
  :root {
    --ink-blue: #4b62a3;
    --text-grey: #6b6b6b;
    --brand-green: #76b543;
    --brand-blue: #5068a7;
    --panel: rgba(255,255,255,0.86);
    --paper: #ffffff;
  }
  * { margin: 0; padding: 0; box-sizing: border-box; }
  html, body { width: 851px; height: 1200px; overflow: hidden; background: var(--paper); }
  body { position: relative; font-family: "Open Sans", Arial, sans-serif; color: var(--text-grey); }

  .page { position: absolute; left: 81px; width: 693px; height: 490px; overflow: hidden; }
  .page--cover { top: 95px; }
  .page--inside { top: 637px; border: 1px solid #d6d6d6; background: var(--paper); }

  .cover-photo {
    position: absolute; inset: 0;
    background:
      linear-gradient(180deg, rgba(0,0,0,0) 60%, rgba(178,130,80,0.55) 100%),
      linear-gradient(105deg, #ebe8e4 0%, #f6f5f3 45%, #e9e9e9 70%, #d8d8d8 100%);
  }
  .brand-box {
    position: absolute; left: 370px; top: 0; width: 147px; height: 74px;
    background: var(--paper);
    display: flex; align-items: center; justify-content: center; gap: 6px;
  }
  .brand-mark { width: 10px; height: 10px; background: var(--brand-green); }
  .brand-name {
    font-family: "Catamaran", sans-serif; font-weight: 300; font-size: 15px;
    line-height: 1.05; color: var(--ink-blue);
  }

  .panel { position: absolute; background: var(--panel); }
  .panel--about { left: 0; top: 92px; width: 324px; height: 290px; padding: 18px 34px 0; }
  .panel--title { left: 369px; top: 92px; width: 324px; height: 130px; padding: 18px 24px 0; }

  .section-title {
    font-family: "Catamaran", sans-serif; font-weight: 300;
    color: var(--ink-blue); font-size: 19px; line-height: 1.1; margin-bottom: 9px;
  }
  .body-copy { font-size: 7.6px; line-height: 1.27; margin-bottom: 4px; }
  .body-copy--accent { color: var(--ink-blue); }
  .contact-block { margin-top: 16px; }

  .claim {
    font-family: "Catamaran", sans-serif; font-weight: 300; color: #777;
    font-size: 18px; line-height: 1.13;
  }
  .claim-sub {
    font-family: "Catamaran", sans-serif; font-weight: 400; color: var(--ink-blue);
    font-size: 18.5px; margin-top: 6px;
  }
  .photo-credit { position: absolute; left: 14px; top: 463px; font-size: 7.6px; color: #fff; }

  .services { position: absolute; left: 30px; top: 30px; width: 300px; }
  .services .section-title { font-size: 18px; margin-bottom: 6px; }
  .service-list { list-style: none; font-size: 7.8px; line-height: 13.4px; margin-bottom: 16px; }
  .service-list li { padding-left: 15px; text-indent: -8px; }
  .service-list li::before { content: "•"; margin-right: 5px; font-size: 6px; }

  .planning-photo {
    position: absolute; left: 0; top: 298px; width: 343px; height: 192px;
    background: linear-gradient(160deg, #ffffff 0%, #f0f0f0 45%, #d9d9d9 70%, #e9a23a 85%, #f4f4f4 100%);
  }
  .tile { position: absolute; width: 175px; height: 163px; }
  .tile--a { left: 343px; top: 0; background: linear-gradient(180deg, #e8e8e6, #dcd7cf); }
  .tile--b { left: 343px; top: 163px; width: 350px; background: linear-gradient(100deg, #c8a37a 0%, #ece8e2 45%, #dcdad4 70%, #8a9a6a 100%); }
  .tile--d { left: 518px; top: 326px; background: linear-gradient(180deg, #f2f2f2, #dde3ea); }
  .tile--text {
    display: flex; flex-direction: column; align-items: center; justify-content: center;
    text-align: center; color: #fff;
  }
  .tile--green { left: 518px; top: 0; background: var(--brand-green); }
  .tile--blue { left: 343px; top: 326px; background: var(--brand-blue); }
  .tile-head { font-family: "Catamaran", sans-serif; font-weight: 400; font-size: 18.5px; line-height: 1.1; letter-spacing: 0.5px; }
  .tile-sub { font-family: "Catamaran", sans-serif; font-weight: 400; font-size: 10px; line-height: 1.3; margin-top: 8px; }
  .tile--green .tile-head { margin-top: -12px; }
</style>
</head>
<body>
  <section class="page page--cover">
    <div class="cover-photo" role="img" aria-label="Foto eines hellen Zahnarzt-Behandlungsraums mit Behandlungsstuhl und Holzboden"></div>

    <div class="brand-box">
      <span class="brand-mark"></span>
      <span class="brand-name">Praxisbau<br>Lotse UG</span>
    </div>

    <div class="panel panel--about">
      <h2 class="section-title">Über</h2>
      <p class="body-copy">Jonas Krawinkel, Geschäftsführer der Praxisbau Lotse UG.<br>Industriemeister, Baufachwirt, Betriebswirt (IHK).</p>
      <p class="body-copy">Seit 22 Jahren spezialisiert auf ambulante Einrichtungen des Gesundheitswesens. Ihr übergreifender Spezialist für alle Schnittstellen und Projektetappen.</p>
      <p class="body-copy">Professionelle Unterstützung und Lotse für alle Heilberufe rund um Ihren Praxisstandort. Für Neugründung, Bestandsoptimierung und Standortsuche.</p>
      <p class="body-copy body-copy--accent">Von der Idee bis zur Praxis-Neueröffnung.</p>

      <div class="contact-block">
        <h2 class="section-title">Kontakt</h2>
        <p class="body-copy">Professionelle Unterstützung<br>für Medizin &amp; Dental Praxisbau Lotse UG</p>
        <p class="body-copy">Jonas Krawinkel<br>Lindenauer Weg 18<br>04177 Leipzig</p>
        <p class="body-copy body-copy--accent">info@praxislotse-plan.de<br>www.praxislotse-plan.de</p>
      </div>
    </div>

    <div class="panel panel--title">
      <h1 class="claim">Optimierung und<br>Neuerrichtung<br>medizinischer Einrichtungen</h1>
      <p class="claim-sub">Unsere Leistungen</p>
    </div>

    <p class="photo-credit">Foto: Umsetzung der Praxis Hollerbach &amp; Sternau in Potsdam</p>
  </section>

  <section class="page page--inside">
    <div class="services">
      <h2 class="section-title">Unsere Leistungsbausteine</h2>
      <ul class="service-list">
        <li>Standortsuche, Bewertung, Machbarkeitsprüfung</li>
        <li>Konzeption, Funktionsplanung, Kostenschätzung</li>
        <li>Projektplanung, Terminplanung, Ausbaubeschreibung</li>
        <li>Entwurfs- Einrichtungs- und Ausführungsplanung</li>
        <li>Ausschreibungen, Leistungsvergabe, Schnittstellenmanagement</li>
        <li>Projekt- und Bauüberwachung, bis zur Praxiseröffnung</li>
      </ul>
      <h2 class="section-title">Service</h2>
      <ul class="service-list">
        <li>unabhängige Leistungen, kein Produktverkauf</li>
        <li>Steuerung und Koordination von Gewerken, Dienstleistern und Technikern</li>
        <li>Management Dritter am Projekt Beteiligter (Vermieter, Bauträger, Dental-/ Medizintechnik, IT, Einrichtung, uvm.)</li>
        <li>volle Kosten und Terminkontrolle</li>
        <li>bedarfsgerechte und flexibleBeratung, Unterstützung, Planung</li>
      </ul>
    </div>

    <div class="planning-photo" role="img" aria-label="Foto von Bauplänen mit Tablet, das einen Terminplan zeigt, und einem Bleistift"></div>

    <div class="tile tile--a" role="img" aria-label="Foto eines leeren Rohbauraums mit Fensterreihe"></div>
    <div class="tile tile--text tile--green">
      <p class="tile-head">KONZEPTION<br>PLANUNG<br>UMSETZUNG</p>
      <p class="tile-sub">Expertise, Knowhow,<br>Übersicht</p>
    </div>
    <div class="tile tile--b" role="img" aria-label="Foto eines Praxis-Wartebereichs mit Lederstühlen, Holzlamellen und Olivenbaum"></div>
    <div class="tile tile--text tile--blue">
      <p class="tile-head">MEDIZIN &amp;<br>DENTAL</p>
      <p class="tile-sub">Optimierung und<br>Neuerrichtung medizini-<br>scher Einrichtung</p>
    </div>
    <div class="tile tile--d" role="img" aria-label="Foto eines weißen Praxis-Sterilisationsraums mit Einbauschränken"></div>
  </section>
</body>
</html>
```